Mrs Tidwell

I would like an A5 size two sided flyer designed. This flyer is for handing out and pinningon notice boards. The brochure is prodominately for a male audience and I would prefer that it is not too 'busy'.

My business is complete housekeeping business targeted at fly in fly out miners in WA Australia. The business designs customised packages for the individual or household and completing all work while the person is at work. It is about making life simple for them so when they come home on their break all of the chores are completed and they don't have to do anything. Payments are made by Direct debit on a weekly or fortninghtly basis.

I am looking for bookings to start early 2013 for all areas of Perth.

10% discount on servcies if they included in a package with a regular house clean.

I would not like to see my exact wording from here just put into a design I would like the designer to add some thought to the design..

Please see below a list of my services.

House Cleaning
Regular clean
Spring clean
End of lease or moving clean

Inside
Linen washed
Clothes washed
Clothes ironed
Breakfast basket (Continental)
Breakfast basket (Deluxe)
Dishwashing/drying
Wheelie bins put out and in
Wheelie bins cleaned
Mail collected
Drinks stacked in fridge
Garage cleaned
Windows cleaned
Fridge Cleaned
Oven cleaned
Cupboards cleaned and organised
Carpets steam cleaned
Plants watered

Outside
Lawns mowed
Edges trimmed
Extra garden services
Windows washed
Cobwebs removed
Gutters cleaned
Reticulation maintenance/repairs
Patio area cleaned
Lawn and garden fertilising
Rubbish removal

Other
Alcohol delivery
Meet tradesperson/suppliers
Grocery shopping+
Run errands+
Bills paid+
Send or collect parcels+
Dry cleaning dropped off+
Clothing repairs alterations
Present shopping wrapping, card selection+

Your car
Car washed and vacuumed
Car detailed
Car drop off and collected for service and/or repairs+

Prodominately males and Miners

Shopping

```html
<!DOCTYPE html>
<html lang="en">
<head>
<meta charset="utf-8">
<title>Mrs Tidwell – Complete Housekeeping Services Flyer</title>
<link rel="stylesheet" href="https://fonts.googleapis.com/css2?family=Oswald:wght@700&family=Questrial&family=Ubuntu:ital,wght@0,500;0,700;1,700&display=swap">
<style>
  :root {
    --stage: #d9d5cd;
    --paper: #e7e6e0;
    --red: #d81c1c;
    --red-deep: #7c0a0c;
    --red-mid: #c8181d;
    --charcoal: #262626;
    --ink: #1d1d1d;
    --white: #ffffff;
  }
  * { margin: 0; padding: 0; box-sizing: border-box; }
  html, body {
    width: 1200px;
    height: 900px;
    overflow: hidden;
    background: var(--stage);
  }
  .flyer {
    position: absolute;
    left: 300px;
    top: 25px;
    width: 600px;
    height: 850px;
    background: var(--paper);
    box-shadow: 0 4px 18px rgba(0,0,0,.25);
    overflow: hidden;
    font-family: "Ubuntu", sans-serif;
  }
  .flyer-shapes {
    position: absolute;
    inset: 0;
  }
  .brand-name {
    position: absolute;
    top: 18px;
    left: 0;
    width: 100%;
    text-align: center;
    font-family: "Oswald", sans-serif;
    font-weight: 700;
    font-size: 74px;
    line-height: 1;
    color: var(--red);
    letter-spacing: 1px;
  }
  .brand-rule {
    position: absolute;
    top: 104px;
    left: 70px;
    width: 460px;
    height: 2px;
    background: linear-gradient(90deg, transparent, var(--ink) 15%, var(--ink) 85%, transparent);
  }
  .brand-tagline {
    position: absolute;
    top: 110px;
    left: 0;
    width: 100%;
    text-align: center;
    font-family: "Questrial", sans-serif;
    font-size: 25px;
    color: var(--ink);
  }
  .headline {
    position: absolute;
    top: 178px;
    left: 28px;
    width: 250px;
    text-align: center;
    font-weight: 700;
    color: var(--red);
    line-height: 1.05;
  }
  .headline-you { display: block; font-size: 62px; }
  .headline-rest { display: block; font-size: 35px; }
  .illustration {
    position: absolute;
    left: 250px;
    top: 165px;
    width: 340px;
    height: 360px;
    background: radial-gradient(closest-side, rgba(200,28,28,.35), rgba(30,30,30,.14) 65%, rgba(30,30,30,0) 100%);
  }
  .offer-badge {
    position: absolute;
    left: 16px;
    top: 478px;
    width: 318px;
    height: 128px;
    background: var(--charcoal);
    border: 4px solid var(--red);
    border-radius: 12px;
    box-shadow: 0 0 0 3px var(--white);
    transform: rotate(-3deg);
    color: var(--white);
    text-align: center;
    padding-top: 10px;
  }
  .offer-title { font-weight: 700; font-size: 33px; line-height: 1.1; }
  .offer-detail { font-weight: 500; font-size: 20px; line-height: 1.25; margin-top: 6px; }
  .promise {
    position: absolute;
    left: 16px;
    top: 640px;
    width: 320px;
    color: var(--white);
    font-weight: 700;
    font-style: italic;
    font-size: 17.5px;
    line-height: 1.6;
  }
  .services {
    position: absolute;
    left: 385px;
    top: 578px;
    color: var(--white);
  }
  .services-title {
    font-weight: 700;
    font-size: 20px;
    text-decoration: underline;
    text-underline-offset: 3px;
    margin-left: 15px;
    margin-bottom: 10px;
  }
  .services-list { list-style: none; }
  .services-list li {
    display: flex;
    align-items: center;
    gap: 12px;
    font-weight: 500;
    font-size: 18px;
    height: 30px;
  }
  .services-list li::before {
    content: "";
    width: 8px;
    height: 8px;
    border-radius: 50%;
    background: var(--white);
    margin-left: 8px;
    flex: none;
  }
  .contact {
    position: absolute;
    left: 0;
    top: 790px;
    width: 100%;
    height: 60px;
    color: var(--white);
    text-align: center;
  }
  .contact-phone { font-weight: 700; font-size: 20px; padding-top: 8px; letter-spacing: .5px; }
  .contact-online { font-family: "Questrial", sans-serif; font-size: 15px; margin-top: 4px; letter-spacing: .8px; word-spacing: 6px; }
</style>
</head>
<body>
  <main class="flyer">
    <svg class="flyer-shapes" width="600" height="850" viewBox="0 0 600 850" aria-hidden="true">
      <defs>
        <radialGradient id="redPanel" cx="50%" cy="55%" r="70%">
          <stop offset="0" stop-color="#c8181d"/>
          <stop offset="1" stop-color="#7c0a0c"/>
        </radialGradient>
      </defs>
      <path d="M0,604 Q300,575 600,470 L600,790 L0,790 Z" fill="url(#redPanel)"/>
      <path d="M0,604 Q300,575 600,470" fill="none" stroke="#ffffff" stroke-width="4"/>
      <rect x="0" y="786" width="600" height="4" fill="#ffffff"/>
      <rect x="0" y="790" width="600" height="60" fill="#262626"/>
    </svg>

    <h1 class="brand-name">Mrs Tidwell</h1>
    <div class="brand-rule"></div>
    <p class="brand-tagline">Complete Housekeeping Services</p>

    <h2 class="headline">
      <span class="headline-you">You</span>
      <span class="headline-rest">Don't Have To</span>
      <span class="headline-rest">Do A Thing</span>
    </h2>

    <div class="illustration" role="img" aria-label="Illustration of a housekeeper in a red uniform dusting with a feather duster"></div>

    <div class="offer-badge">
      <p class="offer-title">Get 10% off</p>
      <p class="offer-detail">Include in a package with a<br>regular house clean.</p>
    </div>

    <p class="promise">We are all about making your life simple, So when you come home on your break, all of the chores are completed.</p>

    <section class="services">
      <h3 class="services-title">Major Services:</h3>
      <ul class="services-list">
        <li>House Cleaning</li>
        <li>Regular clean</li>
        <li>Indoor Services</li>
        <li>Outdoor Services</li>
        <li>Car Services</li>
      </ul>
    </section>

    <footer class="contact">
      <p class="contact-phone">Call: 08-5550-2817 or 0412000739</p>
      <p class="contact-online">enquiries@mrstidwell.com.au &nbsp;|&nbsp; www.mrstidwell.com.au</p>
    </footer>
  </main>
</body>
</html>
```